FALCON RIDGE SKY LEISURE SOCIETY

WE MAKE FLYING FUN AGAIN! We are a Semi Government Sport Aviation club that focuses on the highest quality of aviation training but in the spirit of Sport flying. The club is for aviation enthusiasts to come and share their passion with other club members to build their sport pilot skills.
Club Background and Structure: Club is Semi-Government and falls under the Coral Dunes Leisure Authority. We have seven Board Members that Shape the vision of the club. We have a CEO that take care of FRSLS as a whole and an Operations Manager that takes charge of Daily Flight Operations.
SPORT FLYING is different from a normal Pilots license due to the fact that the pilots fly as a hobby and fun and NOT for Commercial purposes . We would like a design to represent a professional but yet fun side of flying to showcase the "club" side (pilot family)
The club focuses on 3 types of Aircraft Fixed wing aircraft, Gyrocopters and Paramotor (NOTE: Paramotor will have their own web page, but the paramotor must be featured as one of the options. when the pilot chooses the paramotor it must link to paramotor web page)
The page must have the following MINIMUM requirements:
1. General page with logo and some nice pictures that feature both aircraft types (photos in files section)
2. "Get Started" tab that features the following sequence a: Choose your aircraft ( picture of Fixed wing and picture of gyrocopter and picture of paramotor)
b: Get a Introductory Flight.
2. "About us"
3. Services & Price
4. Our Team
5. Fleet
6. Bookings (pilots and introductory scenic flights)
7. Events (with calendar please)
8. Contact us
9. FAQ
10 Ground School
11 Other Sports and Activities
12 Our Partners

Requirements
Must have
• Professional design and easy to maintain and user friendlyness
Nice to have
• We have a booking system that needs to be connected to web page if possible
Should not have
• no clip art

```html
<!DOCTYPE html>
<html lang="en">
<head>
<meta charset="utf-8">
<title>Falcon Ridge Sky Leisure Society</title>
<link href="https://fonts.googleapis.com/css2?family=Barlow:wght@300;400;500;600;700&family=Barlow+Condensed:wght@600;700&display=swap" rel="stylesheet">
<style>
:root{
  --pink:#d43f8d;
  --teal:#2aa6c6;
  --navy:#2c3a86;
  --purple:#7a52b0;
  --ink:#3d4556;
  --muted:#8a90a0;
  --line:#e3e6ee;
  --white:#ffffff;
  --soft:#f3f5f9;
}
*{box-sizing:border-box;margin:0;padding:0}
html,body{width:1200px;height:5038px;overflow:hidden}
body{font-family:'Barlow',sans-serif;color:var(--ink);background:var(--white);position:relative}
a{color:inherit;text-decoration:none}

/* header */
.site-header{position:absolute;left:0;top:0;width:1200px;height:120px;background:var(--white);z-index:5}
.topbar{position:absolute;left:430px;top:0;width:770px;height:42px;background:var(--pink);display:flex;align-items:center;gap:20px;padding-left:44px;color:var(--white);font-size:12.5px;font-weight:500;letter-spacing:.3px}
.topbar .phone{margin-left:8px;display:flex;align-items:center;gap:6px;font-weight:600;font-size:14px}
.brand{position:absolute;left:98px;top:18px;display:flex;align-items:center;gap:10px}
.brand-dot{width:34px;height:34px;border-radius:50%;background:var(--purple)}
.brand-name{font-weight:700;font-size:22px;color:var(--navy);line-height:1}
.brand-sub{font-size:9.5px;color:var(--navy);font-weight:600;letter-spacing:.4px;margin-top:4px}
.main-nav a{position:absolute;top:74px;font-size:13.5px;font-weight:500;color:#252c40}
.main-nav a.active::after{content:"";position:absolute;left:0;right:0;top:37px;height:4px;background:var(--pink);border-radius:2px}

/* hero */
.hero{position:absolute;left:0;top:120px;width:1200px;height:590px;background:linear-gradient(120deg,#2d9fc8 0%,#56c3e2 45%,#9fdcef 100%)}
.hero-welcome{position:absolute;left:124px;top:176px;color:var(--white);font-size:24px;font-weight:300;letter-spacing:3px}
.hero-title{position:absolute;left:122px;top:210px;color:var(--white);font-family:'Barlow Condensed',sans-serif;font-weight:700;font-size:54px;line-height:56px;letter-spacing:.5px}
.btn{display:inline-flex;align-items:center;justify-content:center;border-radius:24px;color:var(--white);font-weight:600;font-size:14px;letter-spacing:.4px}
.btn-pink{background:var(--pink)}
.btn-teal{background:#2b7fa8}
.hero .btn{position:absolute;left:124px;top:344px;width:170px;height:46px}
.hero-arrow{position:absolute;top:240px}
.hero-photo{position:absolute;left:470px;top:20px;width:640px;height:500px;border-radius:50%;background:radial-gradient(circle at 55% 55%,rgba(244,200,40,.55),rgba(244,200,40,0) 55%)}

/* soft fade where a cloud border sits */
.cloud-fade{position:absolute;left:0;width:1200px;height:90px;background:linear-gradient(180deg,rgba(255,255,255,0) 0%,rgba(255,255,255,.85) 60%,#fff 100%)}

/* section titles */
.section-title{position:absolute;left:0;width:1200px;display:flex;justify-content:center;align-items:center;gap:10px}
.section-title h2{font-family:'Barlow Condensed',sans-serif;font-weight:700;font-size:40px;color:var(--navy);letter-spacing:.5px}
.wing{width:86px;height:18px;border-radius:18px 2px 18px 2px;background:linear-gradient(90deg,#2c3a86,#9a5bc4)}
.wing.right{transform:scaleX(-1)}
.section-title.light h2{color:var(--white)}
.section-title.light .wing{background:linear-gradient(90deg,rgba(255,255,255,.9),rgba(255,255,255,.5))}

/* aircraft */
.aircraft{position:absolute;top:858px;width:320px;height:320px;border-radius:50%;border:8px solid #8d9098;overflow:hidden}
.aircraft .photo{position:absolute;inset:0}
.aircraft .label{position:absolute;left:0;right:0;top:222px;height:52px;display:flex;align-items:center;justify-content:center;color:var(--white);font-weight:700;font-size:18px;letter-spacing:.3px}

/* about */
.about{position:absolute;left:0;top:1262px;width:1200px;height:640px;background:linear-gradient(180deg,#2aa8d8 0%,#3bbbe6 55%,#7fd3ee 100%)}
.about p{position:absolute;left:210px;top:150px;width:780px;text-align:center;color:var(--white);font-size:16px;line-height:24px}
.about .btn{position:absolute;left:530px;top:274px;width:170px;height:46px}
.about-photo{position:absolute;left:0;top:340px;width:1200px;height:300px;background:linear-gradient(180deg,#9fb7bf 0%,#b93437 35%,#c9363a 70%,#9a2a30 100%)}

/* get started */
.timeline{position:absolute;left:622px;top:2120px;width:3px;height:790px;background:var(--line)}
.step-icon{position:absolute;width:86px;height:86px;border-radius:50%;border:8px solid #f1f2f6;display:flex;align-items:center;justify-content:center}
.step-title{position:absolute;font-size:26px;font-weight:500;color:var(--navy);letter-spacing:.2px}
.step-title::after{content:"";position:absolute;left:0;top:40px;width:58px;height:3px;background:var(--purple)}
.step-text{position:absolute;width:390px;font-size:15.5px;line-height:24.5px;color:#4c5466}
.photo-box{position:absolute;box-shadow:0 6px 18px rgba(0,0,0,.12);border:4px solid var(--white)}
.gs-btn{position:absolute;left:553px;top:2888px;width:170px;height:46px}

/* events */
.events{position:absolute;left:0;top:3014px;width:1200px;height:626px;background:linear-gradient(120deg,#cc3a95 0%,#9b49aa 40%,#6a63c2 70%,#3a8ad6 100%)}
.calendar{position:absolute;left:156px;top:157px;width:412px;height:354px;background:var(--white);border-radius:4px;padding:22px 28px}
.cal-head{display:flex;justify-content:space-between;align-items:center;color:var(--navy);font-size:19px;font-weight:500;letter-spacing:1.5px;padding:0 18px}
.cal-head span{color:#9aa0b0;font-size:18px}
.cal-grid{display:grid;grid-template-columns:repeat(7,1fr);margin-top:30px;row-gap:14px;text-align:center;font-size:12.5px;color:#333a4a}
.cal-grid .dow{color:var(--navy);font-weight:600}
.cal-grid .off{color:#c6cad4}
.cal-grid .today{background:var(--pink);color:var(--white);border-radius:2px;width:34px;margin:0 auto;line-height:24px;margin-top:-4px;height:24px}
.event-card{position:absolute;left:596px;width:396px;height:110px;background:var(--white);border-radius:3px;padding:12px;display:flex;gap:14px}
.event-card .thumb{width:124px;height:86px;flex:none}
.event-card .date{font-size:9.5px;font-weight:600;color:var(--purple);margin-top:8px}
.event-card h3{font-size:12.5px;font-weight:700;color:#262c3c;line-height:17px;margin-top:2px}
.event-card p{font-size:10px;color:var(--muted);margin-top:4px}

/* services */
.services{position:absolute;left:0;top:3640px;width:1200px;height:560px;background:linear-gradient(180deg,#f6f7fa 0%,#e3e7ee 55%,#cdd3dd 100%)}
.services h2{position:absolute;left:122px;top:86px;font-family:'Barlow Condensed',sans-serif;font-weight:700;font-size:36px;line-height:32px;color:var(--navy)}
.services .intro{position:absolute;left:124px;top:180px;width:310px;font-size:15px;line-height:23px;color:#4c5466}
.services .plane{position:absolute;left:92px;top:250px;width:380px;height:180px;background:radial-gradient(ellipse at center,#dfe3ea 0%,#c5ccd7 55%,rgba(205,211,221,0) 72%)}
.service-card{position:absolute;top:100px;width:258px;height:300px;background:var(--white);border-radius:4px;box-shadow:0 4px 14px rgba(40,50,80,.1);padding:8px;text-align:center}
.service-card .thumb{height:170px}
.service-card h3{font-size:16px;font-weight:700;color:var(--navy);margin-top:16px}
.service-card p{font-size:11.5px;line-height:17px;color:#4c5466;margin:8px 16px 0}

/* partners */
.partners-grid{position:absolute;left:96px;top:4334px;width:984px;height:220px;display:grid;grid-template-columns:repeat(5,1fr);grid-template-rows:repeat(2,1fr)}
.partner{display:flex;align-items:center;justify-content:center;gap:8px;font-size:17px;font-weight:600;color:#3a4152;border-right:1px solid var(--line);border-bottom:1px solid var(--line)}
.partner:nth-child(5n){border-right:none}
.partner:nth-child(n+6){border-bottom:none}
.partner .mark{width:14px;height:14px;background:#b8bdc9}

/* footer */
.site-footer{position:absolute;left:0;top:4660px;width:1200px;height:378px;background:var(--soft)}
.footer-brand{position:absolute;left:104px;top:70px;display:flex;align-items:center;gap:14px}
.footer-brand .brand-dot{width:60px;height:60px}
.footer-brand .brand-name{font-size:34px}
.socials{position:absolute;left:246px;top:178px;display:flex;gap:8px}
.socials span{width:30px;height:30px;border-radius:50%;background:var(--purple)}
.foot-col{position:absolute;top:68px}
.foot-col h4{font-size:18px;font-weight:600;color:var(--navy);margin-bottom:14px}
.foot-col li{list-style:none;font-size:13px;color:#4c5466;line-height:26px}
.foot-col li::before{content:"» ";color:var(--navy)}
.contact-row{display:flex;gap:12px;margin-bottom:14px;font-size:13px;line-height:18px;color:#4c5466}
.contact-row .ic{width:30px;height:30px;border-radius:50%;background:var(--purple);flex:none;display:flex;align-items:center;justify-content:center}
.contact-row b{color:var(--navy);font-weight:600}
.copyright{position:absolute;left:0;top:300px;width:1200px;border-top:1px solid #dde1e9;padding-top:28px;text-align:center;font-size:12px;color:#5a6172}
</style>
</head>
<body>

<header class="site-header">
  <div class="topbar">
    <a href="#">FAQ</a><a href="#">GROUND SCHOOL</a><a href="#">OTHER SPORTS AND ACTIVITIES</a><a href="#">OUR PARTNERS</a>
    <span class="phone"><svg width="14" height="14" viewBox="0 0 24 24"><path d="M6.6 10.8a15 15 0 0 0 6.6 6.6l2.2-2.2c.3-.3.7-.4 1-.2 1.1.4 2.3.6 3.6.6.6 0 1 .4 1 1V20c0 .6-.4 1-1 1A17 17 0 0 1 3 4c0-.6.4-1 1-1h3.5c.6 0 1 .4 1 1 0 1.3.2 2.5.6 3.6.1.3 0 .7-.2 1z" fill="#fff"/></svg>(123) 456 7890</span>
  </div>
  <div class="brand">
    <span class="brand-dot"></span>
    <div><div class="brand-name">FRSLS</div><div class="brand-sub">FALCON RIDGE SKY LEISURE SOCIETY</div></div>
  </div>
  <nav class="main-nav">
    <a href="#" class="active" style="left:375px">ABOUT US</a>
    <a href="#" style="left:477px">SERVICE &amp; PRICE</a>
    <a href="#" style="left:629px">OUR TEAM</a>
    <a href="#" style="left:733px">FLEET</a>
    <a href="#" style="left:811px">BOOKINGS</a>
    <a href="#" style="left:918px">EVENTS</a>
    <a href="#" style="left:1006px">CONTACT US</a>
  </nav>
</header>

<section class="hero" role="img" aria-label="Photo of a yellow gyrocopter with two pilots flying over a modern stadium roof">
  <div class="hero-photo"></div>
  <div class="hero-welcome">WELCOME TO FRSLS</div>
  <h1 class="hero-title">FALCON RIDGE SKY<br>LEISURE SOCIETY</h1>
  <a href="#" class="btn btn-pink">GET STARTED ›</a>
  <svg class="hero-arrow" style="left:30px" width="24" height="38" viewBox="0 0 24 38"><path d="M20 3 5 19l15 16" stroke="#fff" stroke-width="4" fill="none"/></svg>
  <svg class="hero-arrow" style="left:1146px" width="24" height="38" viewBox="0 0 24 38"><path d="M4 3l15 16L4 35" stroke="#fff" stroke-width="4" fill="none"/></svg>
</section>
<div class="cloud-fade" style="top:620px" role="img" aria-label="Cloud border ornament"></div>

<div class="section-title" style="top:768px"><span class="wing" role="img" aria-label="Wing ornament"></span><h2>OUR AIRCRAFT</h2><span class="wing right" role="img" aria-label="Wing ornament"></span></div>

<a href="#" class="aircraft" style="left:120px;border-color:#8e929b">
  <div class="photo" role="img" aria-label="Photo of light fixed wing aircraft in a hangar" style="background:linear-gradient(180deg,#cfd4da,#8e959e 60%,#5e646c)"></div>
  <div class="label" style="background:rgba(36,160,196,.95)">FIXED WING AIRCRAFT</div>
</a>
<a href="#" class="aircraft" style="left:460px;border-color:#d23a3f">
  <div class="photo" role="img" aria-label="Photo of a yellow gyrocopter above a red roof" style="background:linear-gradient(160deg,#d8424a,#b8272f 60%,#e0b82a)"></div>
  <div class="label" style="background:rgba(212,63,141,.95)">GYROCOPTERS</div>
</a>
<a href="#" class="aircraft" style="left:800px;border-color:#8c5ab8">
  <div class="photo" role="img" aria-label="Photo of a paramotor pilot and passenger in flight" style="background:linear-gradient(160deg,#c9a37c,#8c6e5a 55%,#e4c23a)"></div>
  <div class="label" style="background:rgba(122,82,176,.95)">PARAMOTOR</div>
</a>

<section class="about">
  <div class="section-title light" style="top:80px"><span class="wing" role="img" aria-label="Wing ornament"></span><h2>ABOUT US</h2><span class="wing right" role="img" aria-label="Wing ornament"></span></div>
  <p>Lorem ipsum dolor sit amet, consectetur adipiscing elit, sed do eiusmod tempor incididunt ut labore et dolore magna aliqua. Ut enim ad minim veniam, quis nostrud exercitation ullamco laboris nisi ut aliquip Ax ea commodo consequat. Duis aute irure dolor in repreh enderit in voluptate velit esse cillum dolore eu fugiat nulla pariatur. Excepteur sint occaecat cupidatat</p>
  <a href="#" class="btn btn-pink">LEARN MORE</a>
  <div class="about-photo" role="img" aria-label="Aerial photo of a gyrocopter flying over a red theme park roof and city skyline"></div>
</section>
<div class="cloud-fade" style="top:1830px" role="img" aria-label="Cloud border ornament"></div>

<div class="section-title" style="top:1950px"><span class="wing" role="img" aria-label="Wing ornament"></span><h2>GET STARTED</h2><span class="wing right" role="img" aria-label="Wing ornament"></span></div>

<div class="timeline"></div>

<h3 class="step-title" style="left:142px;top:2142px">CHOOSE YOUR AIRCRAFT</h3>
<p class="step-text" style="left:144px;top:2196px">Lorem ipsum dolor sit amet, consectetur adipiscing elit, sed do eiusmod tempor incididunt ut labore et dolore magna aliqua. Ut enim ad minim veniam, quis nostrud exercitation ullamco laboris nisi ut aliquip &nbsp;ex ea commodo consequat.</p>
<div class="step-icon" style="left:540px;top:2170px;background:var(--pink)">
  <svg width="34" height="24" viewBox="0 0 34 24"><path d="M3 12h28M17 4v16M10 20h14" stroke="#fff" stroke-width="2.5" fill="none" stroke-linecap="round"/></svg>
</div>
<div class="photo-box" style="left:648px;top:2068px;width:428px;height:310px;background:linear-gradient(150deg,#c83a40,#b0262e 60%,#e2c030)" role="img" aria-label="Photo of a yellow gyrocopter flying over a red roof"></div>
<div class="photo-box" style="left:840px;top:2256px;width:278px;height:196px;background:linear-gradient(180deg,#d5d9de,#9aa1aa 60%,#6a7078)" role="img" aria-label="Photo of a white fixed wing aircraft in a hangar"></div>

<div class="photo-box" style="left:106px;top:2474px;width:430px;height:262px;background:linear-gradient(170deg,#d9b58a,#b5927a 55%,#7d6a63)" role="img" aria-label="Photo of smiling club members standing beside a gyrocopter"></div>
<div class="photo-box" style="left:294px;top:2660px;width:268px;height:190px;background:linear-gradient(160deg,#c9a37c,#8a6f5e 55%,#e2c23a)" role="img" aria-label="Photo of an instructor and guest during an introductory flight"></div>
<div class="step-icon" style="left:582px;top:2582px;background:var(--teal)">
  <svg width="34" height="24" viewBox="0 0 34 24"><path d="M3 12h28M17 4v16M10 20h14" stroke="#fff" stroke-width="2.5" fill="none" stroke-linecap="round"/></svg>
</div>
<h3 class="step-title" style="left:694px;top:2570px">GET A INTRODUCTORY FLIGHT</h3>
<p class="step-text" style="left:696px;top:2626px">Lorem ipsum dolor sit amet, consectetur adipiscing elit, sed do eiusmod tempor incididunt ut labore et dolore magna aliqua. Ut enim ad minim veniam, quis nostrud exercitation ullamco laboris nisi ut aliquip &nbsp;ex ea commodo consequat.</p>

<a href="#" class="btn btn-teal gs-btn">LEARN MORE</a>

<section class="events">
  <div class="section-title light" style="top:64px"><span class="wing" role="img" aria-label="Wing ornament"></span><h2>EVENTS</h2><span class="wing right" role="img" aria-label="Wing ornament"></span></div>
  <div class="calendar">
    <div class="cal-head"><span>‹</span>JUNE 2022<span>›</span></div>
    <div class="cal-grid">
      <div class="dow">SU</div><div class="dow">MO</div><div class="dow">TU</div><div class="dow">WE</div><div class="dow">TH</div><div class="dow">FR</div><div class="dow">SA</div>
      <div class="off">29</div><div class="off">30</div><div class="off">31</div><div>01</div><div>02</div><div>03</div><div>04</div>
      <div>05</div><div>06</div><div>07</div><div>08</div><div>09</div><div>10</div><div>11</div>
      <div>12</div><div>13</div><div>14</div><div>15</div><div>16</div><div>17</div><div>18</div>
      <div>19</div><div>20</div><div>21</div><div>22</div><div>23</div><div>24</div><div>25</div>
      <div>26</div><div>27</div><div>28</div><div><div class="today">29</div></div><div>30</div><div class="off">01</div><div class="off">02</div>
      <div class="off">03</div><div class="off">04</div><div class="off">05</div><div class="off">06</div><div class="off">07</div><div class="off">08</div><div class="off">09</div>
    </div>
  </div>
  <article class="event-card" style="top:156px">
    <div class="thumb" role="img" aria-label="Event photo of a theme park roof from the air" style="background:linear-gradient(160deg,#cfd8de,#c4363c 60%,#8c2a30)"></div>
    <div><div class="date">29 MAY 2022</div><h3>LOREM IPSUM DOLOR SIT<br>AMET CONSECTETUR</h3><p>Sed ut perspiciatis unde omnis iste natus</p></div>
  </article>
  <article class="event-card" style="top:278px">
    <div class="thumb" role="img" aria-label="Event photo of a pilot and passenger in flight" style="background:linear-gradient(160deg,#c9a37c,#8a6f5e 55%,#e2c23a)"></div>
    <div><div class="date">29 MAY 2022</div><h3>LOREM IPSUM DOLOR SIT<br>AMET CONSECTETUR</h3><p>Sed ut perspiciatis unde omnis iste natus</p></div>
  </article>
  <article class="event-card" style="top:400px">
    <div class="thumb" role="img" aria-label="Event photo of a city marina from the air" style="background:linear-gradient(160deg,#a9c4d2,#7c8c8f 55%,#b89a72)"></div>
    <div><div class="date">29 MAY 2022</div><h3>LOREM IPSUM DOLOR SIT<br>AMET CONSECTETUR</h3><p>Sed ut perspiciatis unde omnis iste natus</p></div>
  </article>
</section>

<section class="services" role="img" aria-label="Faded aerial photo of the city skyline behind the service cards">
  <h2>SERVICE<br>AND PRICING</h2>
  <p class="intro">Lorem ipsum dolor sit amet, consectetur adipiscing elit, sed do eiusmo</p>
  <div class="plane" role="img" aria-label="Photo of a white light aircraft in flight"></div>
  <article class="service-card" style="left:477px">
    <div class="thumb" role="img" aria-label="Aerial photo of a waterfront city" style="background:linear-gradient(170deg,#b8cfdc,#8c9ea6 55%,#c9b08a)"></div>
    <h3>Air Flight Service</h3>
    <p>Lorem ipsum dolor sit amet consectet ur adipiscing elit sed do eiusmoLorem ipsum dolor sit amet</p>
  </article>
  <article class="service-card" style="left:754px">
    <div class="thumb" role="img" aria-label="Photo of a yellow gyrocopter in a clear sky" style="background:linear-gradient(170deg,#dfe6ec,#bcc8d2 60%,#e3c23c)"></div>
    <h3>Air Flight Service</h3>
    <p>Lorem ipsum dolor sit amet consectet ur adipiscing elit sed do eiusmoLorem ipsum dolor sit amet</p>
  </article>
  <article class="service-card" style="left:1036px">
    <div class="thumb" role="img" aria-label="Photo of a pilot in a helmet above the desert" style="background:linear-gradient(170deg,#d3dde4,#c7a47e 60%,#a3553e)"></div>
    <h3>Air Flight Service</h3>
    <p>Lorem ipsum dolor sit amet consectet ur adipiscing elit sed do eiusmoLorem ipsum dolor sit amet</p>
  </article>
</section>
<div class="cloud-fade" style="top:4120px" role="img" aria-label="Cloud border ornament"></div>

<div class="section-title" style="top:4250px"><span class="wing" role="img" aria-label="Wing ornament"></span><h2>OUR PARTNER</h2><span class="wing right" role="img" aria-label="Wing ornament"></span></div>

<div class="partners-grid">
  <div class="partner"><span class="mark"></span>Northwind Group</div>
  <div class="partner"><span class="mark"></span>Harbor Capital</div>
  <div class="partner">Oakline &amp; Company</div>
  <div class="partner">Stonebridge</div>
  <div class="partner"><span class="mark"></span>Meridian Equity</div>
  <div class="partner">Larkspur Capital</div>
  <div class="partner"><span class="mark"></span>Tideway Management</div>
  <div class="partner">Summit Hill</div>
  <div class="partner">Ashford Partners</div>
  <div class="partner"><span class="mark"></span>Crestline Associates</div>
</div>

<footer class="site-footer">
  <div class="footer-brand">
    <span class="brand-dot"></span>
    <div><div class="brand-name">FRSLS</div><div class="brand-sub" style="font-size:11px">FALCON RIDGE SKY LEISURE SOCIETY</div></div>
  </div>
  <div class="socials" aria-label="Social links"><span></span><span></span><span></span><span></span></div>
  <div class="foot-col" style="left:453px">
    <h4>QUICK LINKS</h4>
    <ul><li>About us</li><li>Services &amp; Price</li><li>Our Team</li><li>Fleet</li><li>Bookings</li><li>Events</li></ul>
  </div>
  <div class="foot-col" style="left:633px">
    <h4>RESOURCES</h4>
    <ul><li>Contact us</li><li>FAQ</li><li>Ground School</li><li>Other Sports and Activities</li><li>Our Partners</li></ul>
  </div>
  <div class="foot-col" style="left:855px">
    <h4>CONTACT US</h4>
    <div class="contact-row"><span class="ic"><svg width="14" height="16" viewBox="0 0 14 18"><path d="M7 0a7 7 0 0 0-7 7c0 5 7 11 7 11s7-6 7-11a7 7 0 0 0-7-7zm0 10a3 3 0 1 1 0-6 3 3 0 0 1 0 6z" fill="#fff"/></svg></span><div>123 Lorem Ipsum Address line<br>tempor incididunt ut la</div></div>
    <div class="contact-row"><span class="ic"><svg width="14" height="14" viewBox="0 0 24 24"><path d="M6.6 10.8a15 15 0 0 0 6.6 6.6l2.2-2.2c.3-.3.7-.4 1-.2 1.1.4 2.3.6 3.6.6.6 0 1 .4 1 1V20c0 .6-.4 1-1 1A17 17 0 0 1 3 4c0-.6.4-1 1-1h3.5c.6 0 1 .4 1 1 0 1.3.2 2.5.6 3.6.1.3 0 .7-.2 1z" fill="#fff"/></svg></span><div>Phone Number<br><b>(123) 456 7890</b></div></div>
    <div class="contact-row"><span class="ic"><svg width="14" height="12" viewBox="0 0 20 14"><rect x="1" y="1" width="18" height="12" rx="1" fill="none" stroke="#fff" stroke-width="2"/><path d="M1 1l9 7 9-7" stroke="#fff" stroke-width="2" fill="none"/></svg></span><div>Email address<br><b>enquiry@frsls.com</b></div></div>
  </div>
  <div class="copyright">Copyright © 2022 FRSLS &nbsp;| &nbsp;All Rights Reserved</div>
</footer>

</body>
</html>
```